Business Card for Brightmoor Holdings

I am looking for a design for my business card. I need a logo. The company is called Brightmoor Holdings. We are an investment management and technology consulting company. I am looking for a professional conservative design. I think a lighthouse might be a good simple for us.

For the business card.
company URL www.brightmoorholdings.example
my name: Calvin R. Pratt
email: cpratt@brightmoorholdings.example
my phone # 555-301-6947

Contact Information for Business Card

company URL www.brightmoorholdings.example my name: Calvin R. Pratt email: cpratt@brightmoorholdings.example my phone # 555-301-6947

Colors
0054AA
0677BA
7BADD7
CADEEF
E8F1F8

Requirements
Must have
• area on the back for a QR code

```html
<!DOCTYPE html>
<html lang="en">
<head>
<meta charset="utf-8">
<title>Brightmoor Holdings – Business Card</title>
<link rel="stylesheet" href="https://fonts.googleapis.com/css2?family=Fira+Sans:wght@500;600;700&display=swap">
<style>
  :root {
    --card-bg: #2e4560;
    --brand-cyan: #25cfe0;
    --name-teal: #3ee3c3;
    --icon-teal: #35d9bd;
    --text-white: #ffffff;
    --stripe-teal: #2fa293;
  }
  * { box-sizing: border-box; margin: 0; padding: 0; }
  html, body {
    width: 1200px;
    height: 706px;
    overflow: hidden;
    background: var(--card-bg);
  }
  .card {
    position: relative;
    width: 1200px;
    height: 706px;
    background: var(--card-bg);
    overflow: hidden;
    font-family: "Fira Sans", sans-serif;
    color: var(--text-white);
  }
  .card__stripes {
    position: absolute;
    inset: 0;
    width: 1200px;
    height: 706px;
  }
  .brand-name {
    position: absolute;
    left: 111px;
    top: 104px;
    font-size: 60px;
    font-weight: 600;
    letter-spacing: -0.5px;
    color: var(--brand-cyan);
    line-height: 1;
    white-space: nowrap;
  }
  .person {
    position: absolute;
    left: 121px;
    top: 300px;
  }
  .person__name {
    font-size: 46px;
    font-weight: 600;
    color: var(--name-teal);
    letter-spacing: 0.3px;
    line-height: 1;
    text-transform: uppercase;
  }
  .person__title {
    margin-top: 20px;
    font-size: 17px;
    font-weight: 600;
    letter-spacing: 0.2px;
    text-transform: uppercase;
  }
  .qr-slot {
    position: absolute;
    left: 120px;
    top: 446px;
    width: 199px;
    height: 197px;
    border: 4px solid var(--text-white);
    border-radius: 12px;
    display: flex;
    align-items: center;
    justify-content: center;
    text-align: center;
    font-size: 34px;
    font-weight: 600;
    line-height: 1.3;
    text-transform: uppercase;
  }
  .qr-slot__clip {
    position: absolute;
    left: 34px;
    top: -17px;
    width: 123px;
    height: 27px;
    background: var(--text-white);
    border-radius: 5px;
  }
  .contact-list {
    position: absolute;
    left: 680px;
    top: 311px;
    list-style: none;
  }
  .contact-list__item {
    display: flex;
    align-items: center;
    height: 28px;
    margin-bottom: 22px;
    font-size: 20px;
    font-weight: 600;
  }
  .contact-list__icon {
    width: 27px;
    height: 27px;
    margin-right: 21px;
    flex: none;
  }
  .contact-divider {
    position: absolute;
    left: 681px;
    top: 517px;
    width: 61px;
    height: 3px;
    background: var(--text-white);
  }
</style>
</head>
<body>
<div class="card">
  <svg class="card__stripes" viewBox="0 0 1200 706" aria-hidden="true">
    <defs>
      <linearGradient id="stripe-fade" x1="0" y1="1" x2="1" y2="0.3">
        <stop offset="0" stop-color="#2fa293" stop-opacity="0.05"/>
        <stop offset="0.55" stop-color="#2fa293" stop-opacity="0.35"/>
        <stop offset="1" stop-color="#2fa293" stop-opacity="0.05"/>
      </linearGradient>
      <linearGradient id="stripe-strong" x1="0" y1="1" x2="1" y2="0.4">
        <stop offset="0" stop-color="#2fa293" stop-opacity="0.9"/>
        <stop offset="1" stop-color="#2fa293" stop-opacity="0.15"/>
      </linearGradient>
    </defs>
    <polygon points="120,706 300,706 1200,300 1200,230" fill="url(#stripe-fade)"/>
    <polygon points="340,706 600,706 1200,420 1200,310" fill="url(#stripe-strong)" opacity="0.55"/>
    <polygon points="590,706 860,706 1200,545 1200,430" fill="url(#stripe-strong)" opacity="0.8"/>
    <polygon points="880,706 1200,706 1200,560" fill="url(#stripe-strong)" opacity="0.6"/>
  </svg>

  <div class="brand-name">Brightmoor Holdings</div>

  <div class="person">
    <h1 class="person__name">Calvin R. Pratt</h1>
    <p class="person__title">Managing Partner</p>
  </div>

  <div class="qr-slot">
    <span class="qr-slot__clip"></span>
    Your QR<br>Here
  </div>

  <ul class="contact-list">
    <li class="contact-list__item">
      <svg class="contact-list__icon" viewBox="0 0 28 28" aria-hidden="true">
        <circle cx="14" cy="14" r="13" fill="var(--icon-teal)"/>
        <path d="M10 8.5c.6-.5 1.4-.4 1.8.2l1.2 1.9c.3.5.2 1.1-.2 1.5l-.8.7c.6 1.4 1.7 2.6 3.1 3.3l.7-.8c.4-.4 1-.5 1.5-.2l1.9 1.2c.6.4.7 1.2.2 1.8l-.8.9c-.6.6-1.6.8-2.4.4-3.4-1.5-5.9-4.1-7.3-7.4-.3-.8-.1-1.7.5-2.3z" fill="var(--card-bg)"/>
      </svg>
      555-301-6947
    </li>
    <li class="contact-list__item">
      <svg class="contact-list__icon" viewBox="0 0 28 28" aria-hidden="true">
        <circle cx="14" cy="14" r="13" fill="var(--icon-teal)"/>
        <g fill="none" stroke="var(--card-bg)" stroke-width="1.5">
          <circle cx="14" cy="14" r="7"/>
          <ellipse cx="14" cy="14" rx="3" ry="7"/>
          <line x1="7" y1="14" x2="21" y2="14"/>
        </g>
      </svg>
      www.brightmoorholdings.example
    </li>
    <li class="contact-list__item">
      <svg class="contact-list__icon" viewBox="0 0 28 28" aria-hidden="true">
        <circle cx="14" cy="14" r="13" fill="var(--icon-teal)"/>
        <g fill="none" stroke="var(--card-bg)" stroke-width="1.5" stroke-linejoin="round">
          <rect x="7.5" y="9.5" width="13" height="9" rx="1"/>
          <polyline points="7.5,10 14,15 20.5,10"/>
        </g>
      </svg>
      cpratt@brightmoorholdings.example
    </li>
  </ul>

  <div class="contact-divider"></div>
</div>
</body>
</html>
```